We need UI/UX design for a public, informational website for The Copper Lantern.
The pages, structure, and content scope are already defined. Designers are required to work only on the UI/UX layout of these existing pages, focusing on clarity, hierarchy, spacing, and usability. Do not add, remove, rename, or reinterpret pages or content.
The website is strictly informational only. It must not include accounts, onboarding, payments, custody, escrow administration, marketplaces, dashboards, or any transactional functionality.
Scope of work
Apply UI/UX design to the predefined website pages
Design layout for text, images, notices, and sections
Ensure consistent components and layout patterns across page types
Optimize layouts for long form, compliance focused content
Content writing, page creation, and branding changes are out of scope.
Structure reference
The complete page list, hierarchy, and content definitions are provided in the technical documentation and must be treated as the primary source of truth.
A Figma link is provided only as a light visual reference for page existence and structure:
https://maple-kettle-48203917.plansite.example/
Designers must rely on the documentation for in depth and authoritative reference.
Brand guidelines
The Copper Lantern has existing brand guidelines and official logos, including light and dark versions. These assets will be provided and must be followed exactly. Designers must not redesign, alter, or reinterpret the brand identity.
Look and feel direction
The desired visual direction is inspired by:
https://quorvanta.example/
This reference is provided only to indicate:
Institutional and enterprise tone
Clean, modern typography
Strong hierarchy and generous whitespace
Editorial, content first layouts
Do not copy branding, layouts, components, or assets from the reference site.
Hero section direction
The hero section should follow a similar structural approach to the hero used on https://quorvanta.example/
, meaning:
Strong editorial framing
Clear headline hierarchy
Calm, institutional first impression
However, the background video must be Abu Dhabi focused, not generic or global. The video should visually reflect:
Abu Dhabi skyline or architectural language
Institutional, sovereign, long term infrastructure tone
Clean, slow, cinematic motion
No promotional, marketing, or lifestyle visuals
The hero must remain informational, restrained, and credible. No hype. No calls to invest. No implied participation.
Constraints
One global primary CTA only: “Continue to Brightmoor” (external)
All other interactions must be informational
No visuals or language implying offers, investment, eligibility, or participation
Clear separation between informational content and any external operational platforms
Deliverables
High fidelity UI/UX designs created in Figma, covering:
Desktop layouts
Tablet layouts where relevant
Mobile layouts
Complete Figma file(s) including:
All designed pages defined in the technical documentation
A reusable component library (headers, footers, cards, notice panels, forms, CTAs, typography styles, spacing system)
Clearly defined layout grids, spacing rules, and text styles
Proper use of components and variants, not detached frames
Designs prepared for developer handoff, including:
Clear layer naming and structure
Auto layout where appropriate
Consistent use of styles and components
Responsive behavior demonstrated within Figma
Notes or annotations only where necessary for clarity
No prototypes, interactions, or motion design beyond basic layout states, unless explicitly requested. The focus is static UI/UX clarity, not animation.
A detailed technical specification document and official brand assets will be provided.
Any designs delivered outside Figma, that alter structure or content, or that ignore the defined constraints, boundaries, or tone will be rejected.

```html
<!DOCTYPE html>
<html lang="en">
<head>
<meta charset="utf-8">
<title>The Copper Lantern — Governance Intelligence</title>
<link href="https://fonts.googleapis.com/css2?family=Hanken+Grotesk:wght@400;500;600&display=swap" rel="stylesheet">
<style>
:root{
  --backdrop:#b3b3b3;
  --ink:#0d0d0d;
  --muted:#555;
  --soft:#f1f4f9;
  --white:#fff;
  --black:#000;
  --charcoal:#2a2a2a;
  --line:#d6d9de;
  --line-dark:#3a3a3a;
}
*{box-sizing:border-box;margin:0;padding:0}
html,body{width:1200px;height:3543px;overflow:hidden}
body{background:var(--backdrop);font-family:"Hanken Grotesk",Arial,sans-serif;color:var(--ink)}
.page{position:absolute;left:81px;top:81px;width:1038px;box-shadow:0 4px 18px rgba(0,0,0,.25)}
section,footer,header{position:relative;width:1038px}
.abs{position:absolute}
.wrap{position:absolute;left:147px;width:743px}
.pill{display:inline-block;border-radius:20px;font-weight:500;font-size:11px;padding:7px 15px}
.pill-dark{background:var(--black);color:var(--white)}
.eyebrow{font-size:9px;color:#8a8d93}
/* hero */
.hero{height:589px;color:var(--white);overflow:hidden}
.hero-photo{position:absolute;inset:0;background:linear-gradient(180deg,#2e2e2e 0%,#4a4a4a 35%,#3a3a3a 70%,#232323 100%)}
.brand{position:absolute;left:14px;top:10px;display:flex;align-items:center;gap:6px;font-size:11px;font-weight:500;letter-spacing:.5px;color:var(--white)}
.brand-dot{width:46px;height:46px;border:1.5px solid currentColor;border-radius:50%}
.nav{position:absolute;top:20px;left:0;width:100%;display:flex;justify-content:center;gap:30px;font-size:9px;color:#ccc}
.nav .active{color:var(--white);font-weight:600}
.nav-cta{position:absolute;right:11px;top:11px;background:var(--white);color:var(--ink);font-size:9px;padding:5px 10px;border-radius:12px;font-weight:500}
.hero-copy{position:absolute;top:302px;width:100%;text-align:center}
.hero-copy h1{font-size:36px;font-weight:500;line-height:46px;letter-spacing:-.3px}
.hero-copy p{font-size:17px;line-height:26px;color:#e5e5e5;margin-top:14px}
.hero-btn{display:inline-block;margin-top:18px;border:1.5px solid var(--white);border-radius:16px;padding:5px 15px;font-size:11px;font-weight:500}
/* about */
.about{height:889px;background:var(--soft)}
.about h2{font-size:28px;font-weight:500;line-height:33px;letter-spacing:-.3px}
.about-text{width:360px;font-size:8.5px;line-height:14px;color:#333;margin-top:10px}
.tiles{position:absolute;left:537px;top:84px;display:flex;gap:6px}
.tile{width:113px;height:213px;background:linear-gradient(180deg,#5a5a5a,#1c1c1c);position:relative}
.tile span{position:absolute;left:13px;bottom:12px;color:var(--white);font-size:10px;line-height:12px}
.role-head{position:absolute;top:389px;width:100%;text-align:center}
.role-head h2{font-size:28px;margin-top:6px}
.cards{position:absolute;left:147px;top:447px;display:flex;gap:25px}
.card{width:231px;height:357px;background:var(--white)}
.card-photo{height:142px;background:linear-gradient(180deg,#8b8b8b,#3d3d3d)}
.card-body{padding:15px 19px}
.card h3{font-size:17px;font-weight:500;line-height:20px}
.card p{font-size:8.5px;line-height:12.5px;color:#444;margin-top:7px}
.meta{margin-top:8px}
.meta div{display:flex;font-size:7.5px;line-height:10px;padding:4px 0;border-bottom:1px solid var(--line)}
.meta dt{width:60px;color:#555}
.meta dd{font-weight:600}
/* framework */
.framework{height:633px;background:var(--black);color:var(--white)}
.framework h2{font-size:28px;font-weight:500}
.framework .lead{font-size:9px;line-height:15px;width:220px;margin-top:16px}
.principles{position:absolute;left:466px;top:78px;width:424px}
.principle{height:100px;border-bottom:1px solid var(--line-dark);padding-top:0}
.principle+.principle{padding-top:12px}
.principle .num{font-size:8px;color:#aaa}
.principle h3{font-size:17px;font-weight:500;margin-top:4px}
.principle p{font-size:8.5px;line-height:12.5px;color:#bbb;margin-top:6px}
/* reviewers */
.reviewers{height:363px;background:var(--white)}
.center-h2{font-size:28px;font-weight:500;text-align:center}
.center-p{font-size:8.5px;line-height:13px;color:#333;text-align:center}
.rev-cards{position:absolute;left:147px;top:151px;display:flex;gap:20px}
.rev-card{width:171px;height:143px;border:2px solid #d0d0d0;padding:18px 19px}
.rev-card h3{font-size:13px;font-weight:500;line-height:17px}
.rev-card p{font-size:8.5px;line-height:12.5px;color:#444;margin-top:4px}
/* why */
.why{height:387px;background:var(--soft)}
.why-grid{position:absolute;left:147px;top:139px;width:743px;height:193px}
.why-grid .vline{position:absolute;left:371px;top:0;width:1px;height:193px;background:var(--line)}
.why-grid .hline{position:absolute;left:0;top:96px;width:743px;height:1px;background:var(--line)}
.why-item{position:absolute;width:371px;text-align:center;padding:0 40px}
.why-item h3{font-size:13px;font-weight:500}
.why-item p{font-size:8.5px;line-height:12.5px;color:#444;margin-top:6px}
/* cta */
.cta{height:268px;background:var(--charcoal);color:var(--white);text-align:center}
.cta .label{font-size:9px;color:#ccc;letter-spacing:.3px}
.cta h2{font-size:25px;font-weight:500;line-height:29px;margin-top:8px}
.cta p{font-size:10px;line-height:15px;color:#aaa;margin-top:12px}
.cta .pill{background:var(--black);margin-top:12px}
/* footer */
.footer{height:255px;background:var(--black);color:var(--white)}
.footer .brand{left:147px;top:34px;font-size:10px}
.footer .brand-dot{width:42px;height:42px}
.foot-desc{position:absolute;left:149px;top:100px;width:150px;font-size:7.5px;line-height:10px;color:#ccc}
.col{position:absolute;top:37px}
.col h4{font-size:11px;font-weight:500;margin-bottom:8px}
.col li{list-style:none;font-size:7.5px;line-height:10px;color:#ccc;margin-bottom:5px;width:60px}
.foot-line{position:absolute;left:147px;top:185px;width:743px;height:1px;background:var(--line-dark)}
.foot-small{position:absolute;top:207px;font-size:6.5px;line-height:10px;color:#ccc}
</style>
</head>
<body>
<div class="page">

<header class="hero">
  <div class="hero-photo" role="img" aria-label="Aerial skyline of city towers in muted monochrome"></div>
  <div class="brand"><span class="brand-dot"></span>THE COPPER LANTERN</div>
  <nav class="nav"><span class="active">Home</span><span>Framework</span><span>Projects</span><span>Company</span><span>Insights</span><span>Contact</span></nav>
  <span class="nav-cta">Continue to Brightmoor</span>
  <div class="hero-copy">
    <h1>Governance Intelligence for<br>Long-Term Systems</h1>
    <p>Research-driven frameworks and foresight for<br>complex governance environments</p>
    <span class="hero-btn">View Frameworks</span>
  </div>
</header>

<section class="about">
  <div class="wrap" style="top:89px">
    <div class="eyebrow">About The Copper Lantern</div>
    <h2 style="margin-top:6px">From Governance<br>Frameworks to<br>Institutional Insight</h2>
    <p class="about-text">The Copper Lantern examines governance structures, institutional frameworks, and decision-making models across complex project environments. Our work focuses on research, analysis, and the articulation of principles that inform long-term governance thinking without participating in operational execution.</p>
    <span class="pill pill-dark" style="margin-top:12px">Our Framework</span>
  </div>
  <div class="tiles">
    <div class="tile" role="img" aria-label="Tall office tower facade"><span>Clear Role<br>Separation</span></div>
    <div class="tile" role="img" aria-label="Glass tower in monochrome"><span>Independent<br>Governance<br>Principles</span></div>
    <div class="tile" role="img" aria-label="Curved institutional building"><span>Institutional-Grade<br>Standards</span></div>
  </div>
  <div class="role-head">
    <div class="eyebrow">Role Clarity</div>
    <h2>Our Role Within the Governance Landscape</h2>
  </div>
  <div class="cards">
    <article class="card">
      <div class="card-photo" role="img" aria-label="Columned institutional building"></div>
      <div class="card-body">
        <h3>Governance<br>Framework Analysis</h3>
        <p>We study governance frameworks and institutional structures to understand how authority, accountability, and decision rights are defined across complex environments.</p>
        <dl class="meta">
          <div><dt>Category</dt><dd>Governance Research &amp;<br>Frameworks</dd></div>
          <div><dt>Audience</dt><dd>Institutional, Academic &amp;<br>Public Reference</dd></div>
          <div><dt>Disclosure</dt><dd>Informational Use Only · Not<br>Operational or Advisory *</dd></div>
        </dl>
      </div>
    </article>
    <article class="card">
      <div class="card-photo" role="img" aria-label="Modern towers with curved facade"></div>
      <div class="card-body">
        <h3>Operational Boundary<br>Definition</h3>
        <p>This work documents where governance structures stop and execution begins, establishing conceptual boundaries without involvement in management or operations.</p>
        <dl class="meta">
          <div><dt>Category</dt><dd>Governance Research &amp;<br>Frameworks</dd></div>
          <div><dt>Audience</dt><dd>Institutional, Academic &amp;<br>Public Reference</dd></div>
          <div><dt>Disclosure</dt><dd>Informational Use Only · Not<br>Operational or Advisory *</dd></div>
        </dl>
      </div>
    </article>
    <article class="card">
      <div class="card-photo" role="img" aria-label="Waterfront skyline of high-rise towers"></div>
      <div class="card-body">
        <h3>Transaction-Agnostic<br>Perspective</h3>
        <p>Our perspective remains neutral and non-transactional, focused on principles and structural insight rather than financial activity or execution.</p>
        <dl class="meta">
          <div><dt>Category</dt><dd>Governance Research &amp;<br>Frameworks</dd></div>
          <div><dt>Audience</dt><dd>Institutional, Academic &amp;<br>Public Reference</dd></div>
          <div><dt>Disclosure</dt><dd>Informational Use Only · Not<br>Operational or Advisory *</dd></div>
        </dl>
      </div>
    </article>
  </div>
</section>

<section class="framework">
  <div class="wrap" style="top:81px;width:300px">
    <div class="eyebrow">Core Governance Principles</div>
    <h2 style="margin-top:12px">The Framework</h2>
    <p class="lead">A reference framework outlining governance principles, structural boundaries, and institutional design considerations.</p>
  </div>
  <div class="principles">
    <div class="principle"><div class="num">01</div><h3>Role Boundaries</h3><p>Defines conceptual boundaries between governance entities, operational platforms, and execution responsibilities for institutional reference.</p></div>
    <div class="principle"><div class="num">02</div><h3>SPV Structure</h3><p>Outlines reference structures for special purpose vehicles, focusing on isolation, accountability, design, and structural clarity at a framework level.</p></div>
    <div class="principle"><div class="num">03</div><h3>Escrow Model</h3><p>Presents non-operational reference models describing conditional custody concepts and third-party structural roles in governed environments.</p></div>
    <div class="principle"><div class="num">04</div><h3>Records and Registers</h3><p>Documents record-keeping principles, transparency standards, and informational registries used for governance analysis and reference.</p></div>
    <div class="principle"><div class="num">05</div><h3>Risk and Boundaries</h3><p>Explores risk classification principles and boundary definitions used to evaluate responsibility separation in institutional frameworks.</p></div>
  </div>
</section>

<section class="reviewers">
  <div class="wrap" style="top:78px">
    <h2 class="center-h2">For Framework Reviewers</h2>
    <p class="center-p" style="margin-top:6px">This section is intended for institutional, academic, and professional audiences reviewing governance frameworks for reference, comparison, and analytical understanding. Content is provided to support interpretation of governance principles, structural boundaries, and conceptual models without participation in operational or transactional activity.</p>
  </div>
  <div class="rev-cards">
    <div class="rev-card"><h3>Review Governance<br>Structures</h3><p>Explore published frameworks outlining governance models, role separation, and accountability principles.</p></div>
    <div class="rev-card"><h3>Defined Structural<br>Ownership</h3><p>Frameworks clarify responsibility and authority boundaries without operational or transactional execution.</p></div>
    <div class="rev-card"><h3>Operational<br>Independence</h3><p>Execution, asset handling, and platform operations occur outside this site through independent entities.</p></div>
    <div class="rev-card"><h3>Clear Access<br>Boundaries</h3><p>This site provides documentation and reference materials only—no onboarding, custody, or execution.</p></div>
  </div>
</section>

<section class="why">
  <div class="wrap" style="top:64px">
    <h2 class="center-h2">Why The Copper Lantern</h2>
    <p class="center-p" style="margin-top:6px;padding:0 20px">Our work focuses on the research, analysis, and documentation of governance frameworks across complex institutional environments. Our publications emphasize clarity, structural integrity, and long-term perspective, supporting informed understanding of governance systems without assuming operational roles or authority.</p>
  </div>
  <div class="why-grid">
    <div class="vline"></div><div class="hline"></div>
    <div class="why-item" style="left:0;top:28px"><h3>Governance-First Approach</h3><p>We prioritize structural clarity and accountability, treating governance as the foundation—not an afterthought.</p></div>
    <div class="why-item" style="left:372px;top:28px"><h3>Proven Structural Principles</h3><p>Our frameworks are informed by institutional standards across governance, compliance, and long-term infrastructure design.</p></div>
    <div class="why-item" style="left:0;top:125px"><h3>Bridging Structure &amp; Execution</h3><p>We define governance and role boundaries while execution occurs independently through separate operational platforms.</p></div>
    <div class="why-item" style="left:372px;top:125px"><h3>Defined Control &amp; Boundaries</h3><p>Clear limitations ensure responsibilities remain properly scoped, auditable, and enforceable.</p></div>
  </div>
</section>

<section class="cta">
  <div class="wrap" style="top:60px">
    <div class="label">FOR PROJECT ORIGINATORS</div>
    <h2>Governance Frameworks and<br>Reference Materials</h2>
    <p>Published research, structural frameworks, and reference<br>materials for institutional review.</p>
    <span class="pill">Explore Governance Frameworks</span>
  </div>
</section>

<footer class="footer">
  <div class="brand"><span class="brand-dot"></span>THE COPPER LANTERN</div>
  <p class="foot-desc">Governance frameworks, institutional research, and reference materials focused on structural design, boundaries, and long-term governance principles.</p>
  <div class="col" style="left:347px"><h4>Frameworks</h4><ul><li style="width:110px">Framework Overview</li><li>Role Boundaries</li><li>SPV Structure</li><li>Escrow Model</li><li style="width:100px">Records &amp; Registers</li><li style="width:100px">Risk &amp; Boundaries</li></ul></div>
  <div class="col" style="left:485px"><h4>Insights</h4><ul><li>Insights</li><li>Research Publications</li><li>Analysis &amp; Commentary</li></ul></div>
  <div class="col" style="left:589px"><h4>Company</h4><ul><li>About</li><li>Leadership</li><li>Governance</li><li>Press</li><li>Careers</li></ul></div>
  <div class="col" style="left:689px"><h4>Legal &amp; Reference</h4><ul><li>Legal</li><li>Terms of Use</li><li>Privacy Policy</li><li>Cookie Policy</li><li style="width:110px">Disclaimer &amp; Risk Notices</li><li style="width:110px">Acceptable Use Policy</li><li style="width:110px">Accessibility Statement</li><li>Glossary</li></ul></div>
  <div class="col" style="left:841px"><h4>Contact</h4><ul><li>Contact</li><li>Request Information</li><li>Partners</li></ul></div>
  <div class="foot-line"></div>
  <div class="foot-small" style="left:147px;font-size:8px;font-weight:600;color:var(--white)">Jurisdiction &amp; Disclosure</div>
  <div class="foot-small" style="left:275px;width:200px">Registered in the Harbourline Financial District (HFD).<br>Global scope. Jurisdiction-neutral research and foresight.</div>
  <div class="foot-small" style="left:493px;width:230px">This website provides informational and reference materials only.<br>No content constitutes operational, legal, financial, or investment advice.</div>
  <div class="foot-small" style="left:757px;width:133px;text-align:right">© The Copper Lantern. All rights reserved.</div>
</footer>

</div>
</body>
</html>
```